Quarveling stickers design for our main topics (for example: agile and Kanban)

We are looking for sticker design, that will reflect our cooperate identity and can be used for the different topics in our company. We would like to start with our Agile Coaching Offers with a Kanban Sticker saying "stop starting, start finishing", A bad example can be find in the file upload ;)
Check out our homepage to get a feeling for the cooperate identity (www.quarveling.ch)

Target Market(s)

Customers and trainees from our trainings

Industry/Entity Type

Consulting

Colors
0355a3
fbed22

Requirements
Must have
• a cool design thats fits to our customer design
the 2 lines can be changed for future stickers ... like in the example "stop starting, start finishing" and "we show you how"
Nice to have
• -
Should not have
• -

```html
<!DOCTYPE html>
<html lang="en">
<head>
<meta charset="utf-8">
<title>Quarveling Kanban Sticker</title>
<link rel="stylesheet" href="https://fonts.googleapis.com/css2?family=Barlow:wght@400;600;700&display=swap">
<style>
  :root {
    --page: #ffffff;
    --frame-light: #dcecf7;
    --frame-mid: #a9bedd;
    --frame-dark: #6f88bd;
    --divider: #93a9d2;
    --panel: #ffffff;
    --ink: #5e5f61;
    --ink-soft: #4a4b4d;
    --shadow: rgba(40, 40, 40, 0.55);
  }
  html, body {
    margin: 0;
    padding: 0;
    width: 1200px;
    height: 861px;
    overflow: hidden;
    background: var(--page);
  }
  .sticker {
    display: block;
    width: 1200px;
    height: 861px;
  }
  .sticker-text {
    font-family: "Barlow", "Helvetica Neue", Arial, sans-serif;
    fill: var(--ink);
  }
  .handle { font-size: 29px; font-weight: 700; letter-spacing: 0.5px; }
  .slogan { font-size: 29px; font-weight: 700; letter-spacing: 0.2px; }
  .tagline { font-size: 18px; font-weight: 400; }
  .brand-name { font-size: 26px; font-weight: 400; fill: var(--ink-soft); }
</style>
</head>
<body>
<svg class="sticker" viewBox="0 0 1050 753" xmlns="http://www.w3.org/2000/svg" role="img" aria-label="Quarveling Kanban sticker: stop starting, start finishing">
  <defs>
    <linearGradient id="frame-gradient" gradientUnits="userSpaceOnUse" x1="120" y1="0" x2="940" y2="0">
      <stop offset="0" stop-color="var(--frame-light)"/>
      <stop offset="0.45" stop-color="var(--frame-mid)"/>
      <stop offset="1" stop-color="var(--frame-dark)"/>
    </linearGradient>
    <filter id="drop-shadow" x="-10%" y="-10%" width="125%" height="135%">
      <feGaussianBlur in="SourceAlpha" stdDeviation="6"/>
      <feOffset dx="10" dy="14" result="blur"/>
      <feFlood flood-color="var(--shadow)"/>
      <feComposite in2="blur" operator="in"/>
      <feMerge>
        <feMergeNode/>
        <feMergeNode in="SourceGraphic"/>
      </feMerge>
    </filter>
  </defs>

  <g class="sticker-frame" filter="url(#drop-shadow)" fill="url(#frame-gradient)">
    <rect x="218" y="107" width="622" height="300" rx="105"/>
    <rect x="120" y="232" width="820" height="166" rx="83"/>
    <rect x="218" y="300" width="622" height="222" rx="105"/>
  </g>

  <path class="panel-top" fill="var(--panel)"
        d="M243 243 L243 222 Q243 130 345 130 L715 130 Q817 130 817 222 L817 243 Z"/>
  <rect class="panel-brand" x="625" y="257" width="290" height="119" rx="59.5" fill="var(--panel)"/>
  <rect class="panel-blank" x="145" y="257" width="512" height="119" rx="59.5" fill="var(--panel)"/>
  <path class="panel-divider" d="M597.5 257 A59.5 59.5 0 0 1 597.5 376"
        fill="none" stroke="var(--divider)" stroke-width="10"/>
  <path class="panel-bottom" fill="var(--panel)"
        d="M243 386 L817 386 L817 412 Q817 498 715 498 L345 498 Q243 498 243 412 Z"/>

  <text class="sticker-text handle" x="527" y="208" text-anchor="middle">@LEONARD</text>

  <text class="sticker-text brand-name" x="780" y="326" text-anchor="middle">Quarveling</text>

  <text class="sticker-text slogan" x="529" y="434" text-anchor="middle">STOP STARTING, START FINISHING</text>
  <text class="sticker-text tagline" x="529" y="471" text-anchor="middle">WE SHOW YOU HOW ...</text>
</svg>
</body>
</html>
```